Dentistry Office

We want a new design for a Dentist's office website.

The theme is: "We provide high quality, state-of-the-art, dental care in a comfortable, caring environment."

The site currently has a menu on the left of the page with about 40 items on it. There is a great deal of textual content on each page, plus several illustrations.

We want to do this using CSS, so we need specifications in the CSS for all possible elements. The CSS needs to be named in a logical manner for easy use.

Every dentist on the planet seems to use lots of Flash. We don't want to because it is so distracting. We are looking for an elegant solution targeting 24-55 age group, but not excluding anyone.

The following (from another dentist's site) can give you a taste of what we want to communicate on the site:

"After 20 years of teaching dentists how to refine their technique and many years of writing textbooks, I currently devote my time to my office and the hands-on practice of dentistry. I'd like to welcome you personally to my dental practice, and I invite you to meet my highly experienced team of professionals.

"We have offered complete dental care of the highest quality since 1978. We provide Preventive Services, Tooth Whitening and Cosmetic Dentistry for a beautiful smile, Endodontics (root canal treatment) to treat painful teeth, Sedation Dentistry so you can relax, and Dental Implants to restore what is missing. We offer total care.

"Our approach to your health is simple: We use our education, experience and dedication to provide every patient with superior dental care.

"This passion for excellence is not just a goal, but a standard every member of our team holds.

"We also pride ourselves with our state of the art procedures, training and technology. This includes creating a beautiful smile using techniques that preserve as much of the original tooth as possible.

"Our abilities are renowned throughout the dental profession and I hope if you have any questions you will contact us by an e-mail note, by phone or just by dropping by."

Keep in mind the screen shape and dimensions. Your design needs to work in the normal screen proportions, regardless of how it looks when you post it here. Scrolling is OK, but the first impression needs to work.

Keep in mind that there will be about 250 words, or more, on each page.

Competitors web sites:

http://www.brellwickdentist.example/

http://www.brellwickdentalcare.example/

http://www.grinsbybrellwickdental.example/

http://www.dorvanfamilydentalcare.example/

http://www.brellwickdental.example/

http://www.quimbertdental.example/

We need to compete with these.

Target Market(s)

Generally adults seeking the most experienced and comfortable-to-be-with dentist.

Industry/Entity Type

Training

Requirements
Must have
• Must stand apart from other dentists.
• Must be elegant.
• Must have a horizontal menu structure across all columns, NOT a vertical that requires scrolling, no popout, pop down, etc. menus.
• We are looking for something special.
• Do not waste your time or ours putting up templates and things you have used before.
• Personally, I do not see how someone outside the US can understand the northern California dental market. But you are welcome to try.
Should not have
• Flash or graphics that move
• The look of a template
• Folksy fonts
• Looks like you used it 20 times before

```html
<!DOCTYPE html>
<html lang="en">
<head>
<meta charset="utf-8">
<title>Dental Care</title>
<link href="https://fonts.googleapis.com/css2?family=PT+Serif&family=Tinos:wght@400;700&family=PT+Sans&family=Open+Sans&display=swap" rel="stylesheet">
<style>
  :root{
    --page-bg:#eaf4fd;
    --white:#ffffff;
    --lime:#9ac32a;
    --navy:#3d5a9b;
    --orange:#ffaa05;
    --pink:#ee3f8d;
    --heading:#4d4d4d;
    --body-text:#555a60;
    --link:#1f74b8;
    --rule:#e2e2e2;
    --date:#8a8a8a;
    --menu-text:#222222;
  }
  *{margin:0;padding:0;box-sizing:border-box}
  html,body{width:1108px;height:1200px;overflow:hidden;background:var(--page-bg)}
  body{position:relative;font-family:"Open Sans",Verdana,sans-serif;color:var(--body-text)}
  .abs{position:absolute}

  .hero{left:0;top:15px;width:1108px;height:508px;
    background:linear-gradient(100deg,#bcd9ee 0%,#d7e8f3 22%,#c9a58d 40%,#e0b597 60%,#d7a686 78%,#c9957a 100%)}
  .accent-bar{left:127px;top:0;width:215px;height:26px;background:var(--lime)}
  .phone{left:722px;top:0;width:219px;height:46px;background:var(--navy);color:var(--white);
    font-family:"PT Sans",sans-serif;font-size:19px;text-align:center;line-height:40px;letter-spacing:.3px}
  .brand{left:168px;top:86px;font-family:"PT Sans",sans-serif;font-size:38px;color:var(--lime);letter-spacing:.5px}

  /* horizontal main navigation across all columns */
  .main-nav{left:128px;top:475px;width:960px;height:48px;display:flex;background:var(--white)}
  .main-nav-label{width:212px;height:48px;background:var(--orange);color:var(--white);
    font-family:"Tinos",serif;font-weight:700;font-size:13px;line-height:48px;padding-left:29px}
  .main-menu{list-style:none;display:flex;align-items:center;padding-left:32px;gap:0}
  .main-menu li{font-family:"Tinos",serif;font-size:13.5px;color:var(--menu-text);
    padding:0 22px 0 0;margin-right:22px;border-right:1px solid var(--rule);line-height:18px;display:flex;align-items:center}
  .main-menu li:last-child{border-right:none}
  .main-menu li::before{content:"\2192";font-size:9px;color:#999;margin-right:7px}
  .main-menu li.current span{border-bottom:1px solid var(--menu-text)}
  .main-menu li.current::before{color:var(--menu-text)}

  .sidebar{left:128px;top:523px;width:212px;height:632px;background:var(--white)}
  .sermons-head{margin-top:28px;height:49px;background:var(--pink);color:var(--white);padding-left:29px;
    line-height:48px;font-family:"PT Sans",sans-serif;font-size:13.5px;letter-spacing:.3px}
  .sermon-date{position:absolute;left:29px;font-size:8.5px;color:var(--date);display:flex;align-items:center;gap:6px}
  .sermon-date svg{display:block}
  .sermon-rule{position:absolute;left:28px;width:157px;height:1px;background:var(--rule)}

  .section-title{font-family:"PT Serif",serif;font-size:22px;color:var(--heading);font-weight:400}
  .feature-frame{left:371px;top:595px;width:477px;height:145px;border:1px solid #ccd2d8;background:var(--white);padding:2px}
  .feature-photo{width:100%;height:100%;background:linear-gradient(90deg,#6c625a 0%,#c9b9a8 30%,#f0e3d6 50%,#e7e7e8 75%,#d4d4d6 100%)}
  .copy{left:372px;top:748px;width:478px;font-size:10.2px;line-height:13.35px;letter-spacing:.1px}
  .copy p+p{margin-top:13.35px}
  .copy p.tight{margin-top:0}
  .link-list{list-style:none;font-size:10.4px;line-height:17.15px}
  .link-list a{color:var(--link);text-decoration:underline}
  .link-list.arrowed li{padding-left:10px;position:relative}
  .link-list.arrowed li::before{content:"\203A";position:absolute;left:0;top:-1px;color:#777;font-size:11px}
  .copy-links{left:372px;top:1030px}
  .copy-links li{padding-left:9px}
  .copy-links li:first-child::before{content:"\203A";position:absolute;margin-left:-9px;color:#777}

  .services-intro{left:878px;top:602px;width:180px;font-size:10.2px;line-height:13.3px}
  .services-list{left:876px;top:657px}
  .more{left:878px;top:831px;font-size:10.5px;font-weight:700;color:#888;text-decoration:underline}
  .side-photo-a{left:877px;top:870px;width:210px;height:139px;background:linear-gradient(120deg,#e8ddd2,#f7efe9 45%,#e1bfae)}
  .side-photo-b{left:877px;top:1015px;width:211px;height:140px;background:linear-gradient(180deg,#e7eef5 0%,#8fb0cd 50%,#3e6f9f 100%)}
</style>
</head>
<body>
  <div class="abs hero" role="img" aria-label="Photo of smiling young friends on a beach"></div>
  <div class="abs accent-bar"></div>
  <div class="abs phone">ph:0000 0000</div>
  <div class="abs brand">LOGO</div>

  <nav class="abs main-nav">
    <div class="main-nav-label">Main menu</div>
    <ul class="main-menu">
      <li class="current"><span>Home</span></li>
      <li>About Us</li>
      <li>Blog</li>
      <li>Our Mission</li>
      <li>Sermons</li>
      <li>Contacts</li>
    </ul>
  </nav>

  <aside class="abs sidebar">
    <div class="sermons-head">Latest Sermons</div>
    <div class="sermon-date" style="top:123px"><svg width="9" height="9" viewBox="0 0 9 9"><rect x=".5" y=".5" width="8" height="8" fill="none" stroke="#888"/><path d="M2 2l4 4M6 3v3H3" fill="none" stroke="#888"/></svg>FEB 7 | 2010</div>
    <div class="sermon-rule" style="top:175px"></div>
    <div class="sermon-date" style="top:191px"><svg width="9" height="9" viewBox="0 0 9 9"><rect x=".5" y=".5" width="8" height="8" fill="none" stroke="#888"/><path d="M2 2l4 4M6 3v3H3" fill="none" stroke="#888"/></svg>FEB 7 | 2010</div>
    <div class="sermon-rule" style="top:259px"></div>
    <div class="sermon-date" style="top:282px"><svg width="9" height="9" viewBox="0 0 9 9"><rect x=".5" y=".5" width="8" height="8" fill="none" stroke="#888"/><path d="M2 2l4 4M6 3v3H3" fill="none" stroke="#888"/></svg>FEB 7 | 2010</div>
  </aside>

  <h2 class="abs section-title" style="left:372px;top:562px">What We Do</h2>
  <div class="abs feature-frame"><div class="feature-photo" role="img" aria-label="Photo of a smiling girl brushing her teeth with a dentist and assistant"></div></div>
  <div class="abs copy">
    <p>Lorem ipsum dolor sit amet, consec tetuer adipiscing elit. Praesent vestibulum molestie lacus. Aenean nonummy hendrerit mauris. Phasellus porta. Fusce suscipit varius mi. Cum sociis natoque penatibus et magnis dis parturient montes, nascetur ridiculus mus. Nulla dui. Fusce feugiat malesuada odio. Morbi nunc odio, gravida at, cursus nec, luctus a, lorem.</p>
    <p>Maecenas tristique orci ac sem. Duis ultricies pharetra magna. Donec accumsan malesuada orci. Donec sit amet eros. Lorem ipsum dolor sit amet, consectetuer adipiscing elit. Mauris fermentum dictum magna. Sed laoreet aliquam leo. Ut tellus dolor, dapibus eget, elementum vel, cursus eleifend, elit. Aenean auctor wisi et urna. Aliquam erat volutpat. Duis ac turpis. Integer rutrum ante eu lacus</p>
    <p class="tight">Lorem ipsum dolor sit amet, consec tetuer adipiscing elit. Praesent vestibulum molestie lacus. Aenean nonummy hendrerit mauris. Phasellus porta. Fusce suscipit varius mi. Cum sociis natoque penatibus et magnis dis parturient montes, nascetur ridiculus mus. Nulla dui. Fusce feugiat malesuada odio. Morbi nunc odio, gravida at, cursus nec, luctus a, lorem.</p>
    <p>Maecenas tristique orci ac sem. Duis ultricies pharetra magna. Donec accumsan malesuada orci. Donec sit amet eros. Lorem ipsum dolor sit amet, consectetuer adipiscing elit. Mauris fermentum dictum magna. Sed laoreet aliquam leo. Ut tellus dolor, dapibus eget, elementum vel, cursus eleifend, elit. Aenean auctor wisi et urna. Aliquam erat volutpat. Duis ac turpis. Integer rutrum ante eu lacus</p>
  </div>
  <ul class="abs link-list copy-links">
    <li><a>Lorem ipsum dolor sit amet</a></li>
    <li><a>Praesent vestibulum molestie lacus.</a></li>
    <li><a>Aenean nonummy hendrerit mauris.</a></li>
  </ul>

  <h2 class="abs section-title" style="left:876px;top:562px">Services</h2>
  <p class="abs services-intro">Lorem ipsum dolor sit amet, consec tetuer adipiscing elit. Praesent vestibulum molestie lacus.</p>
  <ul class="abs link-list arrowed services-list">
    <li><a>Management Consulting</a></li>
    <li><a>Policy and Regulatory Analysis</a></li>
    <li><a>Market Assessment</a></li>
    <li><a>Program Management</a></li>
    <li><a>Regulatory Support</a></li>
    <li><a>Scientific and Risk Assessment</a></li>
    <li><a>Change Management</a></li>
    <li><a>Information Technology</a></li>
    <li><a>Strategic Communications</a></li>
    <li><a>Training and Education</a></li>
  </ul>
  <a class="abs more">more</a>
  <div class="abs side-photo-a" role="img" aria-label="Photo of a woman brushing her teeth"></div>
  <div class="abs side-photo-b" role="img" aria-label="Photo of toothbrushes and a dental mirror in a cup"></div>
</body>
</html>
```